Animal Eye Clinic needs a Business card

We are a new veterinary ophthalmology practice (Tessaly Animal Eye Care) and we need a business card designed. We only see animal eyes - we are not a regular veterinary clinic. We already have a logo. We are looking for a professional, good looking business card to hand out to our clients. We are looking for something simple but professional and contemporary. Our logo is likely the only picture/graphic that needs to be on the card.
Updates

Contact Information for Business Card

Marisol Dunkley, BSc, DVM, MSc, DipACVO
Veterinary Ophthalmologist

Phone: 250.418.3097
Email: tessalyanimaleyecare@mailbrook.net
Website: tessalyanimaleyecare.net
Address: 1840 Pellworth Rd
Kelowna, BC, V4T 8M3

Colors

Designer to choose colors to be used in the design.

Requirements
Must have
• Our logo (attached)

```html
<!DOCTYPE html>
<html lang="en">
<head>
<meta charset="utf-8">
<title>Tessaly Animal Eye Care — Business Card</title>
<link rel="stylesheet" href="https://fonts.googleapis.com/css2?family=Roboto:wght@400;500;700&display=swap">
<style>
  :root {
    --teal: #0a8aa3;
    --slate: #555557;
    --slate-dark: #464648;
    --paper: #ececec;
    --backdrop: #d9d9d9;
    --white: #ffffff;
    --ink-soft: #e4e4e4;
  }
  * { margin: 0; padding: 0; box-sizing: border-box; }
  html, body {
    width: 1200px; height: 800px; overflow: hidden;
    background: var(--backdrop);
    font-family: "Roboto", Arial, sans-serif;
  }
  .canvas {
    position: relative; width: 1200px; height: 800px;
    display: flex; align-items: center; justify-content: center; gap: 50px;
  }
  .card {
    position: relative; width: 525px; height: 300px; overflow: hidden;
    box-shadow: 0 6px 18px rgba(0,0,0,.18);
  }
  .card--front { background: var(--slate); color: var(--white); }
  .card__bands { position: absolute; inset: 0; }

  .brand {
    position: absolute; display: flex; align-items: center; gap: 10px;
    font-weight: 700; text-transform: uppercase; line-height: 1.1;
  }
  .brand__dot { width: 26px; height: 26px; border-radius: 50%; flex: none; }
  .card--front .brand { left: 30px; top: 40px; font-size: 15px; color: var(--white); }
  .card--front .brand__dot { background: var(--white); }

  .address {
    position: absolute; left: 30px; top: 118px;
    font-size: 11px; line-height: 1.45; color: var(--ink-soft);
  }

  .person { position: absolute; right: 32px; top: 44px; text-align: right; }
  .person__name { font-size: 22px; font-weight: 700; letter-spacing: .5px; text-transform: uppercase; }
  .person__creds, .person__role { font-size: 11px; line-height: 1.5; color: var(--ink-soft); }
  .person__creds { margin-top: 6px; }

  .contacts {
    position: absolute; right: 32px; bottom: 30px;
    list-style: none; display: flex; flex-direction: column; gap: 6px;
  }
  .contacts__item {
    display: flex; align-items: center; justify-content: flex-end; gap: 10px;
    font-size: 11px; color: var(--ink-soft);
  }
  .contacts__icon {
    width: 16px; height: 16px; background: var(--teal); flex: none;
    display: flex; align-items: center; justify-content: center;
  }

  .card--back { background: var(--paper); }
  .card--back .brand {
    left: 50%; top: 50%; transform: translate(-50%, -50%);
    font-size: 26px; color: var(--teal); gap: 14px;
  }
  .card--back .brand__dot { width: 42px; height: 42px; background: var(--teal); }
</style>
</head>
<body>
<main class="canvas">
  <section class="card card--front" aria-label="Business card front">
    <svg class="card__bands" width="525" height="300" viewBox="0 0 525 300" aria-hidden="true">
      <polygon points="160,0 525,0 525,120 315,215" fill="var(--teal)"/>
      <polygon points="0,0 160,0 315,215 0,300" fill="var(--slate)"/>
      <polygon points="0,215 315,215 525,120 525,300 0,300" fill="var(--slate-dark)" opacity=".35"/>
    </svg>

    <div class="brand"><span class="brand__dot"></span><span>Tessaly<br>Animal Eye Care</span></div>

    <address class="address" style="font-style:normal">1840 Pellworth Rd<br>Kelowna, BC, V4T 8M3</address>

    <div class="person">
      <h1 class="person__name">Marisol Dunkley</h1>
      <p class="person__creds">BSc, DVM, MSc, DipACVO</p>
      <p class="person__role">Veterinary Ophthalmologist</p>
    </div>

    <ul class="contacts">
      <li class="contacts__item">250.418.3097
        <span class="contacts__icon"><svg width="10" height="10" viewBox="0 0 10 10"><path d="M2 1 L4 1 L4.5 3 L3.4 3.8 Q4.3 5.7 6.2 6.6 L7 5.5 L9 6 L9 8 Q9 9 8 9 Q1 8.5 1 2 Q1 1 2 1Z" fill="#fff"/></svg></span>
      </li>
      <li class="contacts__item">tessalyanimaleyecare@mailbrook.net
        <span class="contacts__icon"><svg width="10" height="8" viewBox="0 0 10 8"><rect x=".5" y=".5" width="9" height="7" fill="none" stroke="#fff"/><path d="M.5 .5 L5 4.5 L9.5 .5" fill="none" stroke="#fff"/></svg></span>
      </li>
      <li class="contacts__item">tessalyanimaleyecare.net
        <span class="contacts__icon"><svg width="10" height="10" viewBox="0 0 10 10"><circle cx="5" cy="5" r="4.3" fill="none" stroke="#fff" stroke-width=".9"/><ellipse cx="5" cy="5" rx="1.8" ry="4.3" fill="none" stroke="#fff" stroke-width=".8"/><path d="M.7 5 H9.3" stroke="#fff" stroke-width=".8"/></svg></span>
      </li>
    </ul>
  </section>

  <section class="card card--back" aria-label="Business card back">
    <div class="brand"><span class="brand__dot"></span><span>Tessaly<br>Animal Eye Care</span></div>
  </section>
</main>
</body>
</html>
```